2 menu designs: Tarn Hospitality

I have 2 restaurants that are going though large menu changes. I wanted them to have a style change as well!
-one is a steakhouse menu: must fit in two portrait legal pages. there is a picture of the menu book attached. The emphasis of the menu should be on the "steaks" and "prime rib". attached are menu items that need to be included
-the other is a burger restaurant: must fit on one legal landscape page. The focus of this menu should go to the middle of the page and emphasis "burgers" and "fries". attached is the general layout I'm interested in and the menu items that need to be included. Logo for restaurant is also included. picture of restaurant included

Both must be able to be edited often but the number of items and general placement of these items will not change

Industry/Entity Type

Hospitality

```html
<!DOCTYPE html>
<html lang="en">
<head>
<meta charset="utf-8">
<title>Steakhouse Menu – Tarn Hospitality</title>
<link rel="stylesheet" href="https://fonts.googleapis.com/css2?family=Lobster&family=Roboto+Slab:wght@400;700;800&family=Arvo:ital,wght@0,400;0,700;1,700&family=Schoolbell&display=swap">
<style>
:root{
  --red:#c41f2f;
  --gold:#c7a02f;
  --gold-band:#c29d38;
  --ink:#1f1f1f;
  --paper:#ffffff;
  --stage:#ecebe8;
  --script:"Lobster", cursive;
  --slab:"Roboto Slab", serif;
  --serif:"Arvo", serif;
  --hand:"Schoolbell", cursive;
}
*{box-sizing:border-box;margin:0;padding:0}
html,body{width:1200px;height:869px;overflow:hidden}
body{background:var(--stage);position:relative;font-family:var(--slab);color:var(--ink)}
.page{position:absolute;top:24px;width:470px;height:820px;background:var(--paper);box-shadow:0 1px 4px rgba(0,0,0,.15)}
.page-left{left:120px}
.page-right{left:610px}
.frame{position:absolute;border:2px solid var(--red)}
.frame-gold{border-color:var(--gold)}
.script-title{position:absolute;left:50%;top:0;transform:translate(-50%,-55%);background:var(--paper);padding:0 10px;font-family:var(--script);font-weight:400;font-size:34px;color:var(--red);white-space:nowrap;line-height:1}
.frame-gold .script-title{color:var(--gold)}
.item{text-align:center;margin-bottom:7px}
.item-name{font-weight:800;font-size:11.5px;color:var(--red);text-transform:uppercase;line-height:1.15}
.price{color:var(--ink)}
.item-desc{font-family:var(--serif);font-size:8.2px;line-height:1.25;color:var(--ink)}

/* Beginnings */
.beginnings{left:22px;top:44px;width:426px;height:314px}
.beginnings .cols{display:flex;gap:8px;padding:24px 8px 0}
.beginnings .col{flex:1}
.popover{background:var(--gold);color:#fff;text-align:center;padding:4px 6px;margin:4px 4px 0}
.popover-name{font-family:var(--slab);font-weight:800;font-size:17px;line-height:1.1}
.popover-line{font-weight:800;font-size:11.5px;letter-spacing:.5px;line-height:1.2}
.popover-rule{border-top:1.5px solid #fff;margin-top:2px;padding-top:2px}

/* Plat du jour */
.plat{left:26px;top:394px;width:422px;height:254px}
.plat-list{padding:30px 8px 0}
.plat-row{display:flex;align-items:flex-start;margin-bottom:7px}
.plat-day{flex:0 0 80px;text-align:right;padding-right:10px;font-family:var(--serif);font-style:italic;font-weight:700;font-size:13px;color:var(--red)}
.plat-dish{font-weight:800;font-size:11.5px;text-transform:uppercase;line-height:1.15}
.plat-desc{font-family:var(--serif);font-size:7.8px;white-space:nowrap}

/* Kids */
.kids{position:absolute;left:4px;top:666px;width:434px;height:134px;border:2px solid var(--gold);display:flex}
.kids-badge{width:140px;text-align:center;padding-top:6px}
.kids-oval{width:112px;height:74px;border-radius:50%;background:var(--gold);margin:-6px auto 0;color:#fff;font-family:var(--hand);line-height:.95;padding-top:7px}
.kids-oval .kids-word{font-size:30px}
.kids-oval .kids-price{font-size:26px}
.kids-note{font-family:var(--hand);font-size:11px;line-height:1.3;margin-top:4px}
.kids-body{flex:1;text-align:center;padding-top:10px}
.kids-headline{font-weight:800;font-size:13px;color:var(--red)}
.kids-sub{font-family:var(--serif);font-style:italic;font-weight:700;font-size:9.5px;color:var(--red)}
.kids-items{font-weight:800;font-size:12px;line-height:1.25;margin-top:6px}
.kids-choice{font-family:var(--serif);font-style:italic;font-weight:700;font-size:11px;color:var(--gold);line-height:1.2;margin-top:3px}

/* Prime rib */
.prime{position:absolute;left:30px;top:26px;width:410px;height:126px;background:var(--red);color:#fff}
.prime-title{position:absolute;left:8px;top:-6px;background:var(--paper);border:2px solid var(--red);padding:2px 12px;font-family:var(--script);font-weight:400;font-size:30px;color:var(--red);line-height:1.1}
.prime-badge{position:absolute;right:8px;top:14px;font-family:var(--serif);font-weight:700;font-size:9.5px}
.prime-desc{position:absolute;left:0;right:0;top:48px;text-align:center;font-family:var(--serif);font-style:italic;font-weight:700;font-size:10px;line-height:1.35}
.prime-cuts{position:absolute;left:0;right:0;top:82px;display:flex;justify-content:space-around;text-align:center}
.cut-name{font-family:var(--serif);font-weight:700;font-size:14px;color:var(--gold)}
.cut-price{font-family:var(--serif);font-weight:700;font-size:13px}

/* Broiler */
.broiler{position:absolute;left:30px;top:212px;width:410px;height:186px;background:var(--gold-band)}
.broiler-title{position:absolute;left:50%;top:-24px;transform:translateX(-50%);background:var(--paper);border:2px solid var(--gold-band);padding:0 12px;font-family:var(--script);font-weight:400;font-size:32px;color:var(--gold-band);white-space:nowrap;line-height:1.25}
.broiler-intro{position:absolute;top:24px;left:0;right:0;text-align:center;color:#fff;font-family:var(--serif);font-style:italic;font-weight:700;font-size:10px;line-height:1.3}
.steaks{position:absolute;left:14px;top:58px;width:250px;text-align:center}
.steak{font-weight:800;font-size:12px;color:var(--red);margin-bottom:6px;line-height:1.2}
.steak .price{font-size:10.5px;color:var(--ink);font-weight:700}
.steak-sizes{display:block;font-size:10.5px;color:var(--ink)}
.steak-note{font-family:var(--serif);font-style:italic;font-weight:700;font-size:7.5px;color:#fff}
.option-box{position:absolute;right:14px;width:104px;background:var(--paper);text-align:center;padding:4px 4px}
.option-head{font-family:var(--serif);font-style:italic;font-weight:700;font-size:10px;border-bottom:1.5px solid var(--ink);margin:0 6px 2px}
.option-item{font-weight:800;font-size:10px;color:var(--gold-band);line-height:1.2}

/* Sides & entrees */
.sides{left:36px;top:444px;width:176px;height:346px}
.entrees{left:230px;top:444px;width:200px;height:346px}
.sides .script-title,.entrees .script-title{font-size:22px;padding:0 6px}
.list{padding:20px 6px 0}
.list .item-name{color:var(--ink);font-size:10.5px}
.list .item{margin-bottom:8px}
</style>
</head>
<body>

<section class="page page-left" aria-label="Menu left page">
  <div class="frame beginnings">
    <h2 class="script-title">Beginnings</h2>
    <div class="cols">
      <div class="col">
        <div class="item"><h4 class="item-name">Shrimp Louie <span class="price">$18</span></h4><p class="item-desc">Baby Gem Lettuce, Avocado, Little Deviled Egg</p></div>
        <div class="item"><h4 class="item-name">Lamb Ribs <span class="price">$16</span></h4><p class="item-desc">Chimichurri, Herbed Riatta, Feta</p></div>
        <div class="item"><h4 class="item-name">Seasonal Soup <span class="price">MP</span></h4><p class="item-desc">Markets Best, Seasonal Garnish</p></div>
        <div class="item"><h4 class="item-name">Mixed Baby Lettuces <span class="price">$9</span></h4><p class="item-desc">Shaved Market Vegetables,<br>Lemon Herb Vinaigrette</p></div>
        <div class="item"><h4 class="item-name">Heirloom Tomatoes <span class="price">$12</span></h4><p class="item-desc">Buratta Cheese, Basil Essence,<br>Red Wine Vinaigrette</p></div>
        <div class="item"><h4 class="item-name">Roasted Beets <span class="price">$8</span></h4><p class="item-desc">Soft Goat Cheese, Pistachio,<br>Citrus Vinaigrette</p></div>
        <div class="item"><h4 class="item-name">Steakhouse Wedge <span class="price">$8</span></h4><p class="item-desc">Double Cut Bacon, Market Tomato,<br>Bay Coast Blue Cheese Dressing</p></div>
      </div>
      <div class="col">
        <div class="item"><h4 class="item-name">Baby Kale Caesar <span class="price">$9</span></h4><p class="item-desc">Baby Kale, Romaine Hearts, Parmesan,<br>Garlic Brown Butter Crouton,<br>Artichoke Caesar Vinaigrette</p></div>
        <div class="item"><h4 class="item-name">West Coast Oysters <span class="price">$18</span></h4><p class="item-desc">Seasonal Mignonette</p></div>
        <div class="item"><h4 class="item-name">Spiced Poached Shrimp <span class="price">$12</span></h4><p class="item-desc">Classic Cocktail, Green Goddess Dressing</p></div>
        <div class="item"><h4 class="item-name">Double Cute Bacon <span class="price">$8</span></h4><p class="item-desc">Applewood Smoked, Strap Molasses BBQ</p></div>
        <div class="item"><h4 class="item-name">Spinach Artichoke<br>Fondue <span class="price">$8</span></h4><p class="item-desc">Sourdough Crouton, Harbor Spice Chips</p></div>
        <div class="popover">
          <div class="popover-name">MARCO'S</div>
          <div class="popover-line">FAMOUS POP-OVER</div>
          <div class="popover-line popover-rule">COMPLIMENTARY</div>
        </div>
      </div>
    </div>
  </div>

  <div class="frame plat">
    <h2 class="script-title">Plat du Jour</h2>
    <div class="plat-list">
      <div class="plat-row"><span class="plat-day">Sunday</span><div><h4 class="plat-dish">Beef Short Rib</h4><p class="plat-desc">24 Hour Braise, Root Vegetable Hash, Burgundy Reduction</p></div></div>
      <div class="plat-row"><span class="plat-day">Monday</span><div><h4 class="plat-dish">North Beach Cioppino</h4><p class="plat-desc">Shellfish And Spiced Tomato Broth, Crab Toast</p></div></div>
      <div class="plat-row"><span class="plat-day">Tuesday</span><div><h4 class="plat-dish">Sonoma Lamb T-Bone</h4><p class="plat-desc">Roasted Eggplant Caponata, Lamb Jus</p></div></div>
      <div class="plat-row"><span class="plat-day">Wednesday</span><div><h4 class="plat-dish">Coq au Vin</h4><p class="plat-desc">Herb Roasted Breast, Red Wine Braised Thigh, Potato Puree, Root Vegetables</p></div></div>
      <div class="plat-row"><span class="plat-day">Thursday</span><div><h4 class="plat-dish">Day Boat Scallops</h4><p class="plat-desc">Cast Iron Seared, Creamed Sweetcorn, Herbed Lemon Citronette</p></div></div>
      <div class="plat-row"><span class="plat-day">Friday</span><div><h4 class="plat-dish">Beef Short Rib</h4><p class="plat-desc">24 Hour Braise, Root Vegetable Hash, Burgundy Reduction</p></div></div>
      <div class="plat-row"><span class="plat-day">Saturday</span><div><h4 class="plat-dish">North Beach Cioppino</h4><p class="plat-desc">Shellfish And Spiced Tomato Broth, Crab Toast</p></div></div>
    </div>
  </div>

  <div class="kids">
    <div class="kids-badge">
      <div class="kids-oval"><div class="kids-word">Kids</div><div class="kids-price">$6.95</div></div>
      <p class="kids-note">Served with Entrée /<br>Dessert / Drink</p>
    </div>
    <div class="kids-body">
      <p class="kids-headline">Kids under 10 EAT FREE before 7pm</p>
      <p class="kids-sub">— up to 2 kids per each purchased adult entrée —</p>
      <p class="kids-items">CHICKEN TENDERS &nbsp;/&nbsp; MAC &amp; CHEESE<br>BURGER &nbsp;/&nbsp; STEAK &nbsp;/&nbsp; SALMON<br>SEASONAL MIXED VEGETABLES</p>
      <p class="kids-choice">Choice of Fries or Broccoli &amp;<br>Ice Cream Sundae or Fruit</p>
    </div>
  </div>
</section>

<section class="page page-right" aria-label="Menu right page">
  <div class="prime">
    <h2 class="prime-title">Prime Rib</h2>
    <p class="prime-badge">Featuring Certified Heritage Beef®</p>
    <p class="prime-desc">Signature Spice Rubbed, All Day Roasted, Served With Our<br>Baby Iceberg Wedge And Loaded Salt Baked Potato</p>
    <div class="prime-cuts">
      <div><p class="cut-name">QUEEN CUT 14oz</p><p class="cut-price">$28.95</p></div>
      <div><p class="cut-name">PRINCESS CUT 9oz</p><p class="cut-price">$22.95</p></div>
    </div>
  </div>

  <div class="broiler">
    <h2 class="broiler-title">From The Broiler</h2>
    <p class="broiler-intro">Our Heritage Steaks Are Served A La Carte<br>With Our Sea Salt &amp; Crushed Peppercorn Rub</p>
    <div class="steaks">
      <p class="steak">STEAK FRITES AU POIVRE<span class="steak-sizes">6oz $19.95 CHB®</span></p>
      <p class="steak">NY STRIP <span class="price">16oz $38.95 CHB®</span></p>
      <p class="steak">CENTER CUT FILET<span class="steak-sizes">8oz $30.95 | 12oz $34.95</span></p>
      <p class="steak">RIB EYE <span class="price">16oz $33.95 CHB®</span></p>
      <p class="steak-note">CHB® = Featuring Certified Heritage Beef®</p>
    </div>
    <div class="option-box" style="top:60px">
      <p class="option-head">RUBS &amp; SAUCES</p>
      <p class="option-item">PEPPERCORN<br>RED WINE<br>SIGNATURE</p>
    </div>
    <div class="option-box" style="top:126px">
      <p class="option-head">ADD ONS</p>
      <p class="option-item">LOBSTER<br>SHRIMP</p>
    </div>
  </div>

  <div class="frame sides">
    <h2 class="script-title">Seasonal Sides</h2>
    <div class="list">
      <div class="item"><h4 class="item-name">Creamed Spinach $6</h4><p class="item-desc">Bacon Shallot Crumble</p></div>
      <div class="item"><h4 class="item-name">Black Truffle<br>Mac &amp; Cheese $8</h4><p class="item-desc">Micro Broccoli</p></div>
      <div class="item"><h4 class="item-name">Steamed Asparagus $7</h4><p class="item-desc">Garlic Streusel, Lemon Vinaigrette</p></div>
      <div class="item"><h4 class="item-name">Roasted Mushrooms $6</h4><p class="item-desc">Onion Thyme Jus</p></div>
      <div class="item"><h4 class="item-name">Horseradish / Classic<br>Whipped Potatoes $6</h4><p class="item-desc">Creamery Butter</p></div>
      <div class="item"><h4 class="item-name">Salt Baked Potato $6</h4><p class="item-desc">White Cheddar Fondue, Scallions,<br>Smoked Bacon</p></div>
      <div class="item"><h4 class="item-name">Duck Fat Fries $6</h4><p class="item-desc">Sea Salt, Cracked Pepper</p></div>
      <div class="item"><h4 class="item-name">Market Best $6</h4><p class="item-desc">Farm To Table, Changes Daily</p></div>
    </div>
  </div>

  <div class="frame frame-gold entrees">
    <h2 class="script-title">Entrées</h2>
    <div class="list">
      <div class="item"><h4 class="item-name">Seared Pacific<br>Salmon $24</h4><p class="item-desc">Grain Mustard Bearnaise, Seasonal<br>Succotash</p></div>
      <div class="item"><h4 class="item-name">Vegetable<br>Mixed Grill $15</h4><p class="item-desc">Basil Balsamic, Herbed Goat Cheese Crepe</p></div>
      <div class="item"><h4 class="item-name">Petaluma Brick<br>Chicken $19</h4><p class="item-desc">Baby Carrot And Pea Tendril Salad,<br>Roast Chicken Jus</p></div>
      <div class="item"><h4 class="item-name">Westside Frisco Melt</h4><p class="item-desc">Hand Pressed Patty, Grilled Sourdough,<br>White Cheddar, Caramelized Onion,<br>Not So Secret Sauce</p></div>
      <div class="item"><h4 class="item-name">Steakhouse Burger</h4><p class="item-desc">Hand Pressed Patty, Brioche Bun,<br>Lettuce, Tomato, Onion</p></div>
      <div class="item"><h4 class="item-name">Double Cut<br>Pork Chop $21</h4><p class="item-desc">Creamed Cipolini, Pork Jus</p></div>
    </div>
  </div>
</section>

</body>
</html>
```